Take Out and Catering Menu for Authentic Mexican Food Catering Company

I have an Authentic Mexican Food Catering Company. I need to design a cool takeout menu. I have my logo and information . Need help with the layout and design. It's two sided, color , 5.5 x 8.5"
I have attached the sample menu, but please disregard the style of it as it doesn't sit well with me. Although it's traditional Mexican Food I'd like it to be a little more modern than this. Take the Nopal Rojo card as an example of style, font, etc.
The back side can be similar to the one provided, I think the trick is to keep it simple.

Target Market(s)

Target is mostly families as there are family style meals and catering for private events such as graduations, birthdays, etc.

Industry/Entity Type

Catering

Font styles to use
Sans Serif

Colors
9bcb3c
f04a50

Requirements
Must have
• I'd like it to have the word TACOS vertically and in a lighter tone under the Preordered Box Section (so people know that these boxed dinners are to make tacos)
Nice to have
• Maybe a nice undertone image

```html
<!DOCTYPE html>
<html lang="en">
<head>
<meta charset="utf-8">
<title>Casa Cilantro – Takeout &amp; Catering Menu</title>
<link rel="stylesheet" href="https://fonts.googleapis.com/css2?family=Nunito:wght@400;600;700;800;900&display=swap">
<style>
  :root{
    --lime:#9bcb3c;
    --flower:#e8175d;
    --forest:#2f6b4c;
    --sage:#5a6e60;
    --ink:#1f1f1f;
    --paper:#ffffff;
    --backdrop:#eceae6;
    --rule:#9bcb3c;
  }
  *{box-sizing:border-box;margin:0;padding:0}
  html,body{width:1200px;height:1200px;overflow:hidden;background:var(--backdrop);font-family:"Nunito",sans-serif;color:var(--ink)}
  .menu-card{position:absolute;top:250px;width:482px;height:700px;background:var(--paper);overflow:hidden;box-shadow:0 2px 10px rgba(0,0,0,.12)}
  .menu-card--takeout{left:64px}
  .menu-card--catering{left:654px}
  .abs{position:absolute}

  .flower{position:absolute;background:var(--flower);border-radius:50% 10% 50% 10%}

  .brand-frame{position:absolute;left:95px;top:14px;width:314px;height:104px;border:2.5px solid var(--forest);border-radius:18px;text-align:center}
  .brand-name{display:flex;align-items:center;justify-content:center;gap:8px;margin-top:22px;font-weight:800;font-size:30px;color:var(--ink);letter-spacing:.5px}
  .brand-dot{width:12px;height:12px;border-radius:50%;background:var(--flower)}
  .brand-tagline{font-size:11.5px;margin-top:6px}

  .vertical-word{position:absolute;left:2px;top:126px}
  .vertical-word text{font-family:"Nunito",sans-serif;font-weight:900;fill:var(--lime)}

  .section-title{font-weight:800;color:var(--forest);font-size:20px;line-height:19px}
  .note{font-size:9.5px;line-height:11px;color:#444}

  .box-list{position:absolute;left:49px;top:126px;width:205px}
  .box-item{margin-top:8px}
  .box-item h3{font-weight:800;color:var(--flower);font-size:20px;line-height:18.5px}
  .box-item .row{display:flex;justify-content:space-between;align-items:flex-end;margin-top:3px}
  .box-item p{font-size:9.8px;line-height:11px;font-weight:600;width:160px}
  .box-item .price{font-size:9.8px;font-weight:600;line-height:11px}

  .side-col{position:absolute;left:278px;top:135px;width:190px}
  .side-col ul{list-style:none;font-size:10px;line-height:12.4px;font-weight:600;margin-top:4px}
  .order-block{position:absolute;left:278px;top:348px;width:190px}
  .order-call{font-weight:800;color:var(--sage);font-size:21px;line-height:18.5px}
  .phone-big{font-weight:800;color:var(--sage);font-size:26px;margin-top:10px}
  .web{font-weight:800;color:var(--forest);font-size:14.5px;margin-top:4px}
  .address{font-size:11.5px;line-height:14px;color:var(--forest);font-weight:600;margin-top:4px}
  .brand-small{display:flex;align-items:center;gap:6px;font-weight:800;font-size:19px;margin-top:8px}
  .brand-small .brand-dot{width:9px;height:9px}
  .gf-note{position:absolute;left:382px;top:670px;font-size:9.5px;line-height:10px;color:#444}

  .catering-intro{position:absolute;top:154px;font-size:9.2px;line-height:11.1px;font-weight:600;width:118px}
  .catering-intro .cta{color:var(--forest);font-weight:800;margin-top:6px}
  .catering-intro li{list-style:none}
  .leaf{display:inline-block;width:14px;height:6px;border-radius:50%;background:var(--forest);transform:rotate(-25deg);margin-right:3px;vertical-align:middle}

  .pkg-head{position:absolute;top:256px;width:70px;text-align:center;font-size:8.8px;line-height:9.6px;color:var(--forest);font-weight:600}
  .pkg-price{position:absolute;top:291px;width:70px;text-align:center;font-size:9.6px;font-weight:700}
  .pkg-table{position:absolute;left:50px;top:306px;width:400px;border-collapse:collapse}
  .pkg-table td{height:14px;font-size:9.2px;font-weight:600;border-bottom:1.2px solid var(--rule);padding:0;vertical-align:middle}
  .pkg-table td.tick{width:63px;text-align:center}
  .pkg-table td.dish{width:148px}
  .tick svg{width:11px;height:9px;display:block;margin:0 auto}

  .cat-contact{position:absolute;left:50px;top:540px}
  .cat-contact .phone-big{color:var(--forest);margin-top:0;font-size:26px}
  .cat-contact .web{margin-top:0}
  .cat-contact .email{font-weight:800;color:var(--forest);font-size:13.5px;margin-top:3px}
  .cat-contact .phone-small{font-weight:800;color:var(--forest);font-size:12.5px}
  .fine-print{position:absolute;left:305px;top:543px;width:160px;font-size:8.6px;line-height:10.4px;color:#444}
</style>
</head>
<body>
<svg width="0" height="0" style="position:absolute" aria-hidden="true">
  <symbol id="tick" viewBox="0 0 12 10"><polyline points="1.5,4.5 5,8 10.5,1.5" fill="none" stroke="#e8175d" stroke-width="2.2" stroke-linecap="round" stroke-linejoin="round"/></symbol>
</svg>

<section class="menu-card menu-card--takeout">
  <div class="flower" style="left:-6px;top:-8px;width:86px;height:104px" role="img" aria-label="Red flower illustration with green stem"></div>
  <div class="flower" style="left:418px;top:322px;width:70px;height:72px" role="img" aria-label="Red flower illustration with green stem"></div>
  <div class="flower" style="left:264px;top:618px;width:96px;height:86px" role="img" aria-label="Red flower illustration with curling green vine"></div>

  <div class="brand-frame">
    <div class="brand-name">Casa Cilantro <span class="brand-dot"></span></div>
    <div class="brand-tagline">A little taste of Mexico</div>
  </div>

  <svg class="vertical-word" width="40" height="566" aria-label="Tacos Tacos Tacos">
    <text x="-566" y="34" transform="rotate(-90)" font-size="45" textLength="564" lengthAdjust="spacingAndGlyphs">TACOS TACOS TACOS</text>
  </svg>

  <div class="box-list">
    <h2 class="section-title">Pre-ordered<br>Specialty Boxes</h2>
    <p class="note" style="margin-top:5px">Each dinner makes 8 Tacos<br>Reheat time aprox 10 minutes</p>

    <div class="box-item"><h3>Chicken Tinga</h3>
      <div class="row"><p>Includes Flour Tortillas, Crema, Salsa, Charro Beans and Rice</p><span class="price">$36.00</span></div></div>
    <div class="box-item"><h3>Roasted Pork<br>Carnitas</h3>
      <div class="row"><p>Includes Corn Tortillas, Salsa Verde, Charro Beans and Rice</p><span class="price">$36.00</span></div></div>
    <div class="box-item"><h3>Beef Fajitas</h3>
      <div class="row"><p>Includes Corn Tortillas, Salsa Verde, Charro Beans and Rice</p><span class="price">$36.00</span></div></div>
    <div class="box-item"><h3>Green<br>Chicken Tinga</h3>
      <div class="row"><p>Includes Flour Tortillas, Crema, Charro Beans and Rice</p><span class="price">$36.00</span></div></div>
    <div class="box-item"><h3>Chipotle<br>Garlic Shrimp</h3>
      <div class="row"><p>Includes Flour Tortillas, Chipotle Crema, Charro Beans and Rice</p><span class="price">$39.00</span></div></div>
    <div class="box-item"><h3>Chicken Enchiladas</h3>
      <div class="row"><p>Layers of Corn Tortillas, Shredded Chicken, Roasted Corn, Poblano Peppers, Green Enchilada Sauce, Lots of Crema and Melted Cheese, Charro Beans and Rice</p><span class="price">$35.00</span></div></div>
    <div class="box-item"><h3>Vegetarian<br>Enchiladas</h3>
      <div class="row"><p>Layers of Corn Tortillas, Roasted Corn, Poblano Peppers, Green Enchilada Sauce, Lots of Crema and Melted Cheese, Charro Beans and Rice</p><span class="price">$35.00</span></div></div>
  </div>

  <div class="side-col">
    <h2 class="section-title">Available<br>In Store</h2>
    <ul><li>Chicken Tinga Dinner Box</li><li>Carnitas Dinner Box</li></ul>
    <h2 class="section-title" style="margin-top:8px">Extras/Sides</h2>
    <ul><li>Fresh Salsas</li><li>Homemade Chips</li><li>Fresh Guacamole</li><li>Variety of Tortillas</li><li>Mexican Crema</li><li>Assortment of Mexican Cheese</li><li>Cilantro Mousse</li><li>Weekly Specials</li></ul>
  </div>

  <div class="order-block">
    <p class="order-call">Order by<br>phone or<br>online<br>by 2:00pm<br>for same day<br>pick up</p>
    <p class="phone-big">555 014-2290</p>
    <p class="web">www.casacilantro.example</p>
    <p class="address">48 Elm Row, Millbrook NJ 07999<br>In Elm Row Wine Cellars by Harlow</p>
    <div class="brand-small">Casa Cilantro <span class="brand-dot"></span></div>
  </div>
  <p class="gf-note">*ALL GF except<br>for flour tortillas</p>
</section>

<section class="menu-card menu-card--catering">
  <div class="flower" style="left:-6px;top:-8px;width:86px;height:104px" role="img" aria-label="Red flower illustration with green stem"></div>
  <div class="flower" style="left:446px;top:36px;width:44px;height:100px" role="img" aria-label="Red flower illustration"></div>
  <div class="flower" style="left:340px;top:604px;width:120px;height:100px" role="img" aria-label="Red flower illustration with green stem"></div>

  <div class="brand-frame">
    <div class="brand-name">Casa Cilantro <span class="brand-dot"></span></div>
    <div class="brand-tagline">A little taste of Mexico</div>
  </div>

  <svg class="vertical-word" width="44" height="566" aria-label="Catering Catering">
    <text x="-566" y="36" transform="rotate(-90)" font-size="45" textLength="560" lengthAdjust="spacingAndGlyphs">CATERING CATERING</text>
  </svg>

  <h2 class="section-title abs" style="left:49px;top:130px">Catering</h2>
  <ul class="catering-intro" style="left:50px">
    <li>Create your own gourmet taco bar from our authentic menu or choose from one of our 4 pre-designed packages.</li>
    <li class="cta">Contact us to start planning your next event!</li>
  </ul>
  <ul class="catering-intro" style="left:190px;width:122px">
    <li><span class="leaf"></span>Total party planning services available to include beverage selection, rentals, decorations, party favors, etc. to make your event truly authentic and unique!</li>
  </ul>
  <ul class="catering-intro" style="left:326px;width:120px">
    <li><span class="leaf"></span>Hire the taco cart for a fun twist!</li>
    <li style="margin-top:4px"><span class="leaf"></span>We will deliver, set up and decorate with a traditional Mexican flair!</li>
    <li><span class="leaf"></span>Service staff available upon request.</li>
  </ul>

  <h2 class="section-title abs" style="left:50px;top:268px;font-size:21px">Menu</h2>
  <div class="pkg-head" style="left:196px;top:260px">ORIGINAL<br>TACO BAR</div>
  <div class="pkg-head" style="left:259px;top:260px">FIESTA<br>PACK</div>
  <div class="pkg-head" style="left:322px;top:260px">AMIGOS<br>PACK</div>
  <div class="pkg-head" style="left:385px">The WHOLE<br>ENCHILADA<br>PACK</div>
  <div class="pkg-price" style="left:196px">$22.00pp</div>
  <div class="pkg-price" style="left:259px">$24.00pp</div>
  <div class="pkg-price" style="left:322px">$26.00pp</div>
  <div class="pkg-price" style="left:385px">$29.00pp</div>

  <table class="pkg-table">
    <tr><td class="dish">Homemade Chips</td><td class="tick"><svg><use href="#tick"/></svg></td><td class="tick"><svg><use href="#tick"/></svg></td><td class="tick"><svg><use href="#tick"/></svg></td><td class="tick"><svg><use href="#tick"/></svg></td></tr>
    <tr><td class="dish">Nopal Rojo and Chipotle Salsa</td><td class="tick"><svg><use href="#tick"/></svg></td><td class="tick"><svg><use href="#tick"/></svg></td><td class="tick"><svg><use href="#tick"/></svg></td><td class="tick"><svg><use href="#tick"/></svg></td></tr>
    <tr><td class="dish">Chicken Tinga</td><td class="tick"><svg><use href="#tick"/></svg></td><td class="tick"><svg><use href="#tick"/></svg></td><td class="tick"><svg><use href="#tick"/></svg></td><td class="tick"><svg><use href="#tick"/></svg></td></tr>
    <tr><td class="dish">Pork Carnitas</td><td class="tick"><svg><use href="#tick"/></svg></td><td class="tick"><svg><use href="#tick"/></svg></td><td class="tick"><svg><use href="#tick"/></svg></td><td class="tick"><svg><use href="#tick"/></svg></td></tr>
    <tr><td class="dish">Charro Beans</td><td class="tick"><svg><use href="#tick"/></svg></td><td class="tick"><svg><use href="#tick"/></svg></td><td class="tick"><svg><use href="#tick"/></svg></td><td class="tick"><svg><use href="#tick"/></svg></td></tr>
    <tr><td class="dish">Roasted Corn and peppers</td><td class="tick"><svg><use href="#tick"/></svg></td><td class="tick"><svg><use href="#tick"/></svg></td><td class="tick"><svg><use href="#tick"/></svg></td><td class="tick"><svg><use href="#tick"/></svg></td></tr>
    <tr><td class="dish">Corn and Flour Tortillas</td><td class="tick"><svg><use href="#tick"/></svg></td><td class="tick"><svg><use href="#tick"/></svg></td><td class="tick"><svg><use href="#tick"/></svg></td><td class="tick"><svg><use href="#tick"/></svg></td></tr>
    <tr><td class="dish">Crema and Cotija Cheese</td><td class="tick"><svg><use href="#tick"/></svg></td><td class="tick"><svg><use href="#tick"/></svg></td><td class="tick"><svg><use href="#tick"/></svg></td><td class="tick"><svg><use href="#tick"/></svg></td></tr>
    <tr><td class="dish" colspan="2">Appetizer (empanadas or quesadillas)</td><td class="tick"><svg><use href="#tick"/></svg></td><td class="tick"><svg><use href="#tick"/></svg></td><td class="tick"><svg><use href="#tick"/></svg></td></tr>
    <tr><td class="dish">Churros</td><td class="tick"></td><td class="tick"><svg><use href="#tick"/></svg></td><td class="tick"><svg><use href="#tick"/></svg></td><td class="tick"><svg><use href="#tick"/></svg></td></tr>
    <tr><td class="dish">Guacamole</td><td class="tick"></td><td class="tick"></td><td class="tick"><svg><use href="#tick"/></svg></td><td class="tick"><svg><use href="#tick"/></svg></td></tr>
    <tr><td class="dish">Shaved Steak Fajitas</td><td class="tick"></td><td class="tick"></td><td class="tick"><svg><use href="#tick"/></svg></td><td class="tick"><svg><use href="#tick"/></svg></td></tr>
    <tr><td class="dish">Chipotle Garlic Shrimp</td><td class="tick"></td><td class="tick"></td><td class="tick"></td><td class="tick"><svg><use href="#tick"/></svg></td></tr>
    <tr><td class="dish">2 Appetizers</td><td class="tick"></td><td class="tick"></td><td class="tick"></td><td class="tick"><svg><use href="#tick"/></svg></td></tr>
    <tr><td class="dish">Cilantro Lime Rice</td><td class="tick"></td><td class="tick"></td><td class="tick"></td><td class="tick"><svg><use href="#tick"/></svg></td></tr>
    <tr><td class="dish" colspan="4">Fancy Churros (In chocolate cup with dulce de leche)</td><td class="tick"><svg><use href="#tick"/></svg></td></tr>
  </table>

  <div class="cat-contact">
    <p class="phone-big">555 014-2290</p>
    <p class="web">www.casacilantro.example</p>
    <p class="email">hola@casacilantro.example</p>
    <p class="phone-small">555 014-7731</p>
    <p class="address" style="margin-top:3px">48 Elm Row, Millbrook NJ 07999<br>In Elm Row Wine Cellars by Harlow</p>
    <div class="brand-small" style="margin-top:6px">Casa Cilantro <span class="brand-dot"></span></div>
  </div>
  <p class="fine-print">Includes Delivery, Setup and Décor.<br>Serving Trays, (pots, baskets and sarape tablecloths upon request)<br>Includes Serving Utensils, Plates, Forks and Napkins.</p>
</section>
</body>
</html>
```